Outpatient Mental Health Clinic needs a good brochure

We are an outpatient clinic in Michigan, USA and provide therapy and evaluation services for adults, adolescents, and children. Our psychologists, social workers, and counselors help individuals who present with a host of psychological difficulties. Our goal for the brochure is to give an overview of our services so that our marketing person can pass them out to physicians and other referral sources.

Target Market(s)

Our target market are patients who are seeking referrals through their primary care physicians.

Industry/Entity Type

Clinic

Font styles to use
Serif
Sans Serif

Colors
fbf289
f68d4c
f37122
ffffff

Requirements
Must have
• My project must be illustrative enough to show what services are provided. Pictures of individuals is also important.
Nice to have
• In addition to content I would like to have pictures of individuals.

```html
<!DOCTYPE html>
<html lang="en">
<head>
<meta charset="utf-8">
<title>Outpatient Clinic Brochure Spread</title>
<link href="https://fonts.googleapis.com/css2?family=Oswald:wght@600&family=Fira+Sans:wght@400&display=swap" rel="stylesheet">
<style>
  :root {
    --backdrop: #d3d3d3;
    --paper: #fdfdf5;
    --accent: #f68d1e;
    --accent-light: #f9b26b;
    --band-start: #ffd500;
    --band-end: #f68d1e;
    --ink: #3a3a3a;
    --crop: #9a9a9a;
  }
  html, body { margin: 0; padding: 0; width: 1200px; height: 1200px; overflow: hidden; background: var(--backdrop); }
  .stage { position: relative; width: 1500px; height: 1500px; transform: scale(0.8); transform-origin: 0 0; }
  .crop { position: absolute; background: var(--crop); }
  .crop.v { width: 1px; height: 25px; }
  .crop.h { height: 1px; width: 25px; }
  .spread { position: absolute; left: 25px; top: 233px; width: 1450px; height: 1032px; background: var(--paper); overflow: hidden; }
  .wave { position: absolute; left: 0; top: 0; width: 1450px; height: 260px; }
  .photo { position: absolute; left: 0; top: 397px; width: 962px; height: 635px;
    background:
      linear-gradient(180deg, rgba(253,253,245,1) 0%, rgba(253,253,245,0) 22%),
      linear-gradient(180deg, #eef2f6 0%, #c9d3de 45%, #5d6b84 75%, #2f3b55 100%); }
  .heading { position: absolute; margin: 0; font-family: "Oswald", sans-serif; font-weight: 600; font-size: 29px; line-height: 1; color: var(--accent); letter-spacing: 0.5px; white-space: nowrap; }
  .copy { position: absolute; font-family: "Fira Sans", sans-serif; font-size: 15.5px; line-height: 20.3px; color: var(--ink); white-space: nowrap; }
  .copy p { margin: 0 0 20.3px; }
</style>
</head>
<body>
<div class="stage">
  <span class="crop v" style="left:39px;top:208px"></span>
  <span class="crop v" style="left:1460px;top:208px"></span>
  <span class="crop h" style="left:0;top:246px"></span>
  <span class="crop h" style="left:1475px;top:246px"></span>
  <span class="crop v" style="left:39px;top:1265px"></span>
  <span class="crop v" style="left:1460px;top:1265px"></span>
  <span class="crop h" style="left:0;top:1250px"></span>
  <span class="crop h" style="left:1475px;top:1250px"></span>

  <div class="spread">
    <svg class="wave" viewBox="0 0 1450 260" aria-hidden="true">
      <defs>
        <linearGradient id="band" x1="0" y1="0" x2="1" y2="0">
          <stop offset="0" stop-color="var(--band-start)"/>
          <stop offset="1" stop-color="var(--band-end)"/>
        </linearGradient>
      </defs>
      <path d="M0,0 H1450 V100 C1380,170 1250,205 1050,200 C700,190 300,30 0,68 Z" fill="var(--accent-light)"/>
      <path d="M0,0 H1450 V35 C1370,120 1250,176 1050,176 C750,176 300,25 0,56 Z" fill="url(#band)"/>
    </svg>

    <div class="photo" role="img" aria-label="Photo of a group therapy session: a man stands in the centre while seated participants of different ages applaud him"></div>

    <h2 class="heading" style="left:53px;top:114px">WHO WE HELP</h2>
    <div class="copy" style="left:53px;top:163px;width:420px">
      <p>Our outpatient clinic in Michigan offers therapy and<br>evaluation services for adults, adolescents and<br>children. Psychologists, social workers and licensed<br>counselors work together to support each patient<br>with care that fits their needs and goals.</p>
      <p>We help people facing anxiety, depression, stress,<br>grief, trauma, attention and learning concerns,<br>family conflict and life changes. Every plan starts<br>with listening, so care begins where you are.</p>
    </div>

    <div class="copy" style="left:526px;top:142px;width:420px">
      <p>Families<br>are welcome<br>too. We work with parents<br>and schools when it helps a child. Our<br>team coordinates with primary care physicians so<br>treatment stays connected and clear. Appointments<br>are offered on weekdays and some evenings, and<br>most major insurance plans are accepted. We send<br>referring physicians a summary after the first visit<br>and keep them informed as care moves forward,<br>always with the patient's written consent.</p>
    </div>

    <h2 class="heading" style="left:1000px;top:247px">OUR SERVICES</h2>
    <div class="copy" style="left:1000px;top:296px;width:420px">
      <p>Individual therapy for adults, adolescents and<br>children, including cognitive behavioral therapy,<br>supportive counseling and skills-based treatment.<br>Group therapy offers peer support in a safe,<br>guided setting led by experienced clinicians.</p>
      <p>Psychological evaluations clarify diagnosis and<br>guide treatment. We assess ADHD, learning<br>differences, mood and anxiety disorders, autism<br>spectrum concerns and memory changes. Each<br>evaluation ends with a written report and a<br>feedback session to review results and next<br>steps. Family and couples therapy help improve<br>communication, resolve conflict and strengthen<br>relationships at home and at school.</p>
    </div>

    <h2 class="heading" style="left:1000px;top:631px">REFERRING A PATIENT</h2>
    <div class="copy" style="left:1000px;top:680px;width:420px">
      <p>Physicians can refer patients by phone, fax or<br>secure message. Please include the reason for<br>referral, recent medical history and insurance<br>details. Our intake coordinator contacts the<br>patient within two business days to schedule a<br>first visit and answer questions about cost,<br>coverage and what to expect. Patients may also<br>call us directly to request an appointment.<br>With consent, we share evaluation results and<br>treatment updates with the referring office so<br>care stays coordinated. Urgent needs are<br>reviewed the same day, and we help connect<br>patients to crisis services whenever needed.</p>
    </div>
  </div>
</div>
</body>
</html>
```